Anzeigengestaltung für Finanzierungsberatung und Bankenkommunikation
Zielgruppe
Beratung für mittelständische Unternehmen, Schwerpunkt Finanzierungsberatung und Bankenkommunikation
Motto: Mit Kreditgebern auf Augenhöhe kommunizieren
Beratungsschwerpunkte:
- Mittelstandsfinanzierung
- Baufinanzierung
- Existenzgründerfinanzierung
Aufgabenstellung
Mit Kreditgebern auf Augenhöhe kommunizieren als Leitsatz
persönliche Note sollte rüber kommen, ich mache Werbung in einer Region, wo mich die Zielgruppe noch persönlich aus der Bank kennt. Daher ist mir eine Anzeige mit Foto wichtig.
Anzeigenformat
Breite 90mm
Höhe 60 mm

```html
<!DOCTYPE html>
<html lang="de">
<head>
<meta charset="utf-8">
<title>KreditKlar – Anzeige</title>
<link href="https://fonts.googleapis.com/css2?family=Lato:wght@300;400;700&display=swap" rel="stylesheet">
<style>
  :root {
    --purple: #7a2f7e;
    --grey-text: #6b6b6b;
    --panel: #efeff0;
    --frame: #2a2a2a;
    --photo-light: #d9d6d4;
    --photo-dark: #8a7d78;
    --paper: #ffffff;
  }
  * { box-sizing: border-box; }
  html, body {
    margin: 0;
    padding: 0;
    width: 1200px;
    height: 789px;
    overflow: hidden;
    background: var(--paper);
    font-family: "Lato", Arial, sans-serif;
  }
  body { position: relative; }
  .ad {
    position: absolute;
    left: 14px;
    top: 14px;
    width: 1172px;
    height: 761px;
    border: 2px solid var(--frame);
    background: var(--paper);
    overflow: hidden;
  }
  .ad-photo {
    position: absolute;
    left: 14px;
    top: 14px;
    width: 440px;
    height: 729px;
    background: linear-gradient(160deg, var(--photo-light) 0%, #c9c3c0 55%, var(--photo-dark) 100%);
  }
  .brand-box {
    position: absolute;
    left: 454px;
    top: 14px;
    right: 14px;
    height: 180px;
    border: 1.5px solid #9a9a9a;
    border-left: none;
    background: var(--panel);
  }
  .brand-name {
    position: absolute;
    right: 38px;
    top: 48px;
    font-weight: 300;
    font-size: 84px;
    letter-spacing: 1px;
    color: var(--purple);
    line-height: 1;
  }
  .claim-band {
    position: absolute;
    left: 440px;
    top: 210px;
    right: 40px;
    height: 310px;
    background: var(--purple);
    color: #fff;
    padding: 26px 40px 0 34px;
  }
  .claim-title {
    margin: 0 0 22px;
    font-weight: 700;
    font-size: 43px;
    line-height: 1.12;
  }
  .focus-list {
    list-style: none;
    margin: 0;
    padding: 0;
    font-weight: 700;
    font-size: 31px;
    line-height: 1.45;
  }
  .focus-list li {
    display: flex;
    align-items: center;
    gap: 16px;
  }
  .focus-list svg { width: 24px; height: 24px; flex: none; }
  .contact {
    position: absolute;
    margin: 0;
    font-style: normal;
    font-weight: 400;
    color: var(--grey-text);
    white-space: nowrap;
    line-height: 1.4;
  }
  .contact-address { left: 490px; top: 556px; font-size: 31px; }
  .contact-direct { left: 818px; top: 604px; font-size: 29px; }
</style>
</head>
<body>
  <article class="ad">
    <div class="ad-photo" role="img" aria-label="Porträtfoto der Beraterin, sitzend in heller Kleidung vor grauem Hintergrund"></div>

    <div class="brand-box">
      <div class="brand-name">KreditKlar</div>
    </div>

    <section class="claim-band">
      <h1 class="claim-title">Mit Kreditgebern<br>auf Augenhöhe kommunizieren</h1>
      <ul class="focus-list">
        <li><svg viewBox="0 0 24 24"><path d="M3 13 L9 19 L21 5" fill="none" stroke="#fff" stroke-width="3.5" stroke-linecap="round" stroke-linejoin="round"/></svg>Mittelstandsfinanzierung</li>
        <li><svg viewBox="0 0 24 24"><path d="M3 13 L9 19 L21 5" fill="none" stroke="#fff" stroke-width="3.5" stroke-linecap="round" stroke-linejoin="round"/></svg>Baufinanzierung</li>
        <li><svg viewBox="0 0 24 24"><path d="M3 13 L9 19 L21 5" fill="none" stroke="#fff" stroke-width="3.5" stroke-linecap="round" stroke-linejoin="round"/></svg>Existenzgründerfinanzierung</li>
      </ul>
    </section>

    <address class="contact contact-address">
      Jana-Marie Holler<br>
      Lindenweg 4<br>
      31135 Hildesheim
    </address>

    <address class="contact contact-direct">
      0163 – 418 27 05<br>
      info@kreditklar.de<br>
      www.kreditklar.de
    </address>
  </article>
</body>
</html>
```